Car Dealership needs Custom Graphics for new Website/Advertising

We would like 10 or so editable Graphics files for our new website but that we can also edit to use on Facebook, Advertising etc.. I have uploaded our Logo and 2 Graphics we have found that we like the look of. One of the primary advertisements we want is to Buy Cars, hence the two examples. If you are using examples of cars, it is important a variety of car brands are represented i.e. do not just have Brantley or Valmonde cars. We would also like some templates that we could edit to highlight Car of the Week, Free Delivery and other services we offer. All Graphics should have a distinct theme that fits to each other and our website.

Our new website address is http://stage4.pinecrestweb.example/harborautos2/ - this is currently under construction so will be changing daily. Please note the fonts, colors and design layout.

Our current/old website is www.harborautos.example

Harbor Autos is a specialized car dealership selling vehicles to US Military personnel stationed overseas in Germany. Please bear this in mind when designing Graphics.

Please do not use Uncle Sam in any of the designs - we are moving away from this in our new website.

Target Market(s)

US Military Personnel and Families stationed in Germany and Europe

Font styles to use
Sans Serif

Requirements
Must have
• Fresh, consistant design that works well with new website. Ads will be primarily featured in the carousel box on the home page of the site, so should scale apporpriately.
Should not have
• Uncle Sam

```html
<!DOCTYPE html>
<html lang="en">
<head>
<meta charset="utf-8">
<title>Harbor Autos – Carousel Banners</title>
<link rel="stylesheet" href="https://fonts.googleapis.com/css2?family=Saira:wght@400;800&display=swap">
<style>
  :root {
    --page-bg: #ffffff;
    --red-bright: #c8000c;
    --red-mid: #9e0008;
    --red-deep: #5c0b06;
    --red-band: #a3000a;
    --tab-red: #b8000b;
    --text-light: #ffffff;
    --border: #d6d6d6;
  }
  html, body {
    margin: 0;
    padding: 0;
    width: 1200px;
    height: 1000px;
    overflow: hidden;
    background: var(--page-bg);
    font-family: "Saira", "Arial Narrow", sans-serif;
  }
  .banner-stack {
    position: relative;
    width: 1200px;
    height: 1000px;
  }
  .banner {
    position: absolute;
    left: 334px;
    width: 544px;
    height: 288px;
    display: block;
  }
  .banner--buy { top: 31px; outline: 1px solid var(--border); }
  .banner--week { top: 351px; }
  .banner--delivery { top: 670px; }
  .headline {
    font-family: "Saira", "Arial Narrow", sans-serif;
    font-weight: 800;
    fill: var(--text-light);
  }
  .subline {
    font-family: "Saira", "Arial Narrow", sans-serif;
    font-weight: 400;
    fill: var(--text-light);
  }
  .panel { fill: url(#panelGradient); }
  .panel-band { fill: var(--red-band); opacity: 0.85; }
  .panel-tab { fill: var(--tab-red); }
  .panel-line { stroke: #e0101a; stroke-width: 2; opacity: 0.6; fill: none; }
</style>
</head>
<body>
<main class="banner-stack">

  <!-- We Buy Cars -->
  <svg class="banner banner--buy" viewBox="0 0 953 505" preserveAspectRatio="none">
    <defs>
      <linearGradient id="panelGradient" x1="0.3" y1="0" x2="1" y2="1">
        <stop offset="0" stop-color="#c8000c"/>
        <stop offset="0.55" stop-color="#a8000a"/>
        <stop offset="1" stop-color="#5c0b06"/>
      </linearGradient>
      <linearGradient id="showroomTones" x1="0" y1="0" x2="1" y2="1">
        <stop offset="0" stop-color="#eef1f4"/>
        <stop offset="0.5" stop-color="#8b8f97"/>
        <stop offset="1" stop-color="#c9ccd1"/>
      </linearGradient>
      <linearGradient id="sportsCarTones" x1="0" y1="0" x2="1" y2="1">
        <stop offset="0" stop-color="#1a1c24"/>
        <stop offset="0.45" stop-color="#1f4fc4"/>
        <stop offset="1" stop-color="#2a2a2e"/>
      </linearGradient>
      <linearGradient id="workshopTones" x1="0" y1="0" x2="1" y2="1">
        <stop offset="0" stop-color="#b9a89a"/>
        <stop offset="0.5" stop-color="#5d6c8c"/>
        <stop offset="1" stop-color="#3a3a40"/>
      </linearGradient>
    </defs>
    <rect role="img" aria-label="Photo: row of new cars parked in a bright showroom" width="953" height="505" fill="url(#showroomTones)"/>
    <polygon class="panel" points="680,0 953,0 953,505 375,505"/>
    <polygon class="panel-band" points="680,0 775,0 485,505 420,505 430,440"/>
    <polygon class="panel-tab" points="625,95 665,95 585,220 640,220 580,258 495,258"/>
    <line class="panel-line" x1="770" y1="8" x2="478" y2="505"/>
    <text class="subline" x="902" y="150" font-size="84" text-anchor="end">WE</text>
    <text class="headline" x="902" y="265" font-size="128" text-anchor="end">BUY</text>
    <text class="headline" x="898" y="382" font-size="128" text-anchor="end">CARS</text>
    <text class="subline" x="898" y="433" font-size="38" text-anchor="end">Any Make / Any Model</text>
  </svg>

  <!-- Car of the Week -->
  <svg class="banner banner--week" viewBox="0 0 953 505" preserveAspectRatio="none">
    <rect role="img" aria-label="Photo: front of a blue sports coupe with orange wheels" width="953" height="505" fill="url(#sportsCarTones)"/>
    <polygon class="panel" points="680,0 953,0 953,505 375,505"/>
    <polygon class="panel-band" points="680,0 775,0 485,505 420,505 430,440"/>
    <polygon class="panel-tab" points="625,95 665,95 595,162 690,162 560,258 495,258"/>
    <line class="panel-line" x1="770" y1="8" x2="478" y2="505"/>
    <text class="headline" x="913" y="175" font-size="107" text-anchor="end">CAR</text>
    <text class="headline" x="913" y="278" font-size="107" text-anchor="end">OF THE</text>
    <text class="headline" x="913" y="375" font-size="107" text-anchor="end">WEEK</text>
    <text class="subline" x="917" y="435" font-size="44" text-anchor="end">KESTREL K3 GT</text>
  </svg>

  <!-- Free Delivery -->
  <svg class="banner banner--delivery" viewBox="0 0 953 505" preserveAspectRatio="none">
    <rect role="img" aria-label="Photo: mechanic and customer reviewing paperwork in a workshop" width="953" height="505" fill="url(#workshopTones)"/>
    <polygon class="panel" points="680,0 953,0 953,505 375,505"/>
    <polygon class="panel-band" points="680,0 775,0 485,505 420,505 430,440"/>
    <polygon class="panel-tab" points="620,92 665,92 590,165 690,165 560,298 465,298"/>
    <line class="panel-line" x1="770" y1="8" x2="478" y2="505"/>
    <text class="headline" x="930" y="192" font-size="86" text-anchor="end">FREE</text>
    <text class="headline" x="930" y="277" font-size="86" text-anchor="end">DELIVERY</text>
    <text class="subline" x="926" y="337" font-size="45" text-anchor="end">FOR ORDERS</text>
    <text class="subline" x="926" y="382" font-size="45" text-anchor="end">OVER $20.000</text>
  </svg>

</main>
</body>
</html>
```